Fernwick Digital Marketing Agency Website Design. I need a new website for my digital marketing agency. It needs to be FAST and easy to use. I want to be able to add videos to the main homepage like this page: https://www.lumatreeweb.example/search-marketing/cleveland-ohio-seo-companyI'd like to have the request quote tab on the top right side as well as my number above it. The following website is my favorite overall: http://www.vantorelgroup.example/ I'd love to copy something like that.

***** Website I want to copy: http://www.vantorelgroup.example/services/ ******
Updates

This needs to be a Wordpress website. Sorry for any confusion as this is the first time using MakerQuill. I need the homepage as described as well as a Services Page and Contact Us page. Services page should be simply yet creative with a spot for me to insert up to 8 services.

Target Market(s)

Business owners

Industry/Entity Type

Digital Marketing

Coding

Coded - Design and coding required

Number of Pages Required

3 page

Font styles to use
Other font styles liked:
• Oswald

Colors

Designer to choose colors to be used in the design.

Requirements
Must have
• I need to have a nice design/template to work off of in Wordpress. It needs to be bright and vibrant yet elegant in design.
Nice to have
• CTA at the top right as well as a place for the phone number. http://www.vantorelgroup.example/services/

```html
<!DOCTYPE html>
<html lang="en">
<head>
<meta charset="utf-8">
<title>Fernwick Digital Marketing Agency – Home</title>
<link href="https://fonts.googleapis.com/css2?family=Oswald:wght@400;500;600&family=Source+Sans+3:wght@400;600;700&display=swap" rel="stylesheet">
<style>
:root{
  --gold:#eaa91f;
  --gold-bright:#f6b01a;
  --purple:#4a1c86;
  --purple-deep:#2d1158;
  --purple-footer:#3a1570;
  --ink:#2a1050;
  --text:#333;
  --white:#fff;
  --grey:#f1f1f3;
}
*{margin:0;padding:0;box-sizing:border-box}
html,body{width:1200px;height:1200px;overflow:hidden;background:var(--white)}
.stage{position:absolute;left:0;top:0;width:1500px;height:1500px;transform:scale(.8);transform-origin:0 0}
.page{position:absolute;left:473px;top:0;width:552px;height:1500px;font-family:"Source Sans 3",sans-serif;color:var(--text);overflow:hidden}
.abs{position:absolute}
.center{left:0;width:552px;text-align:center}

/* header */
.site-header{top:0;left:0;width:552px;height:37px;background:linear-gradient(90deg,#e6a31c,#edb22a 50%,#e6a31c)}
.brand{left:80px;top:9px;display:flex;align-items:center;gap:4px}
.brand-dot{width:14px;height:14px;border-radius:50%;background:var(--ink)}
.brand-name{font-family:"Oswald",sans-serif;font-weight:500;font-size:12px;line-height:11px;color:var(--ink)}
.brand-tag{font-family:"Oswald",sans-serif;font-weight:500;font-size:5.5px;color:var(--ink);line-height:7px}
.main-nav{left:285px;top:15px;display:flex;gap:9px;font-size:5px;color:var(--white)}
.btn{display:flex;align-items:center;justify-content:center;font-family:"Oswald",sans-serif;font-size:5px;letter-spacing:.2px;color:var(--white);text-transform:uppercase}
.btn-purple{background:var(--purple)}
.btn-gold{background:var(--gold-bright);color:var(--ink)}
.header-cta{left:418px;top:12px;width:59px;height:14px}

/* hero */
.hero{top:37px;left:0;width:552px;height:203px;background:linear-gradient(135deg,#8a8683,#6f6a68 40%,#5d5a5e 70%,#77716c)}
.hero-title{top:73px;font-family:"Oswald",sans-serif;font-weight:500;font-size:21px;color:#f5c21b;letter-spacing:.3px}
.hero-sub{top:100px;font-family:"Oswald",sans-serif;font-size:19px;color:var(--white)}
.play{left:260px;top:146px}

/* services */
.section-title{top:266px;font-family:"Oswald",sans-serif;font-weight:500;font-size:18px;color:#3f1f7a}
.section-sub{top:293px;font-size:12px}
.card{top:333px;width:127px;height:136px;background:linear-gradient(160deg,#5a2696,#45187e);border:1px solid #6b3aa8;border-radius:3px;text-align:center;color:var(--white)}
.card-icon{position:absolute;left:42px;top:21px;width:42px;height:42px;border-radius:50%;background:#7b50b0;display:flex;align-items:center;justify-content:center}
.card-title{position:absolute;left:0;width:100%;top:76px;font-size:6.5px;font-weight:700;letter-spacing:.2px}
.card-text{position:absolute;left:7px;right:7px;top:89px;font-size:5.5px;line-height:9px}
.dash{height:1.5px;width:8px}

/* seo band */
.seo-band{top:549px;left:0;width:552px;height:204px;background:radial-gradient(ellipse at center,#3b1770,#2a0f54 70%,#230c47)}
.seo-title{top:614px;font-family:"Oswald",sans-serif;font-weight:500;font-size:17px;line-height:22px;color:#f5c21b;letter-spacing:.3px}
.seo-text{top:667px;font-size:7px;line-height:14px;color:var(--white)}

/* b2b */
.b2b-title{top:776px;font-family:"Oswald",sans-serif;font-weight:500;font-size:17px;color:var(--ink);letter-spacing:.3px}
.b2b-copy{left:108px;width:337px;text-align:center;font-size:6px;line-height:10.5px;color:#222}
.gallery-label{left:74px;top:909px;font-size:8.5px;font-weight:600;color:var(--purple);letter-spacing:.3px}
.gallery-btn{left:429px;top:911px;width:48px;height:13px}
.shot{top:944px;width:93px;height:105px;border-radius:3px}

/* cta */
.cta{top:1089px;left:0;width:552px;height:204px;background:linear-gradient(100deg,#f4f4f6,#ededf0 55%,#dfe2e8)}
.cta-title{top:1145px;font-family:"Oswald",sans-serif;font-weight:500;font-size:17px;line-height:22px;color:var(--ink);letter-spacing:.3px}
.cta-gold{left:195px;top:1211px;width:93px;height:17px;border-radius:2px}
.cta-purple{left:299px;top:1211px;width:58px;height:17px;border-radius:2px}

/* subscribe */
.subscribe{top:1293px;left:0;width:552px;height:104px;background:linear-gradient(90deg,#f5ab16,#f8b521 50%,#f5ab16)}
.sub-title{top:1314px;font-family:"Oswald",sans-serif;font-weight:500;font-size:10px;color:var(--ink)}
.sub-text{top:1333px;font-size:5.5px;line-height:9px;color:#222}
.field{top:1361px;width:92px;height:11px;background:var(--white);font-size:4px;color:#999;padding:3px 4px}
.sub-btn{left:350px;top:1361px;width:58px;height:12px}

/* footer */
.site-footer{top:1397px;left:0;width:552px;height:103px;background:var(--purple-footer)}
.foot-contact{left:74px;top:1443px;font-size:4.5px;line-height:8px;color:var(--white)}
.social{top:1472px;width:5px;height:5px;border-radius:50%;background:var(--gold-bright)}
.foot-brand{top:1417px;text-align:center;color:#c9c1d9}
.foot-dot{width:22px;height:22px;border-radius:50%;border:2px solid #c9c1d9;margin:0 auto 5px}
.foot-name{font-family:"Oswald",sans-serif;font-size:18px;line-height:18px;letter-spacing:.5px}
.foot-tag{font-family:"Oswald",sans-serif;font-size:8px;line-height:12px}
.foot-links{right:75px;text-align:right;font-size:4.5px;color:var(--white);line-height:8px}
</style>
</head>
<body>
<div class="stage">
<main class="page">

  <header class="site-header abs">
    <div class="brand abs">
      <span class="brand-dot"></span>
      <div><div class="brand-name">FERNWICK</div><div class="brand-tag">Digital Marketing Agency</div></div>
    </div>
    <nav class="main-nav abs"><span>Home</span><span>Services</span><span>Blog</span><span>FAQ</span><span>Contact Us</span></nav>
    <div class="btn btn-purple header-cta abs">Get a free estimate</div>
  </header>

  <section class="hero abs" role="img" aria-label="Desk workspace photo with notebook, coffee, charts and pens"></section>
  <h1 class="hero-title abs center">DIGITAL MARKETING AGENCY</h1>
  <p class="hero-sub abs center">Focused On Results</p>
  <svg class="play abs" width="32" height="32" viewBox="0 0 32 32" aria-label="Play video">
    <circle cx="16" cy="16" r="14.5" fill="none" stroke="#fff" stroke-width="1.4" opacity=".85"/>
    <path d="M13 10.5v11l9-5.5z" fill="none" stroke="#fff" stroke-width="1.3" opacity=".85"/>
  </svg>

  <h2 class="section-title abs center">Fernwick Providing</h2>
  <p class="section-sub abs center">Bussiness Services</p>

  <article class="card abs" style="left:74px">
    <div class="card-icon"><svg width="18" height="18" viewBox="0 0 18 18"><rect x="2" y="2" width="14" height="11" fill="#fff"/><circle cx="9" cy="7.5" r="3.2" fill="none" stroke="#e88a1a" stroke-width="1.6"/><path d="M11.3 9.8l3.5 3.5" stroke="#e88a1a" stroke-width="1.8"/></svg></div>
    <div class="card-title">SEARCH OPTIMIZATION</div>
    <p class="card-text">Whether it's On-Page, Off-Page, Local Citations, or straight up Business Listing Page enhancements, we've got you covered.</p>
  </article>
  <article class="card abs" style="left:212px">
    <div class="card-icon"><svg width="18" height="18" viewBox="0 0 18 18"><rect x="2" y="3" width="14" height="10" fill="#f5b21d"/><rect x="4" y="5" width="10" height="6" fill="#fff"/><path d="M7 13v2h4v-2" fill="#f5b21d"/></svg></div>
    <div class="card-title">SOCIAL MEDIA MARKETING</div>
    <p class="card-text">Let's face it, your company needs a social media presence in today's world. It's no longer a desire, it's now a requirement.</p>
  </article>
  <article class="card abs" style="left:350px">
    <div class="card-icon"><svg width="18" height="18" viewBox="0 0 18 18"><rect x="2" y="3" width="14" height="10" fill="#fff"/><rect x="4" y="5" width="10" height="6" fill="#e88a1a"/><path d="M6 15h6" stroke="#fff" stroke-width="1.5"/></svg></div>
    <div class="card-title">PAID SEARCH ADS</div>
    <p class="card-text">Do you want to take up more space on the real estate of the search results? Are you ready for the increase in customer calls and sales?</p>
  </article>
  <span class="dash abs" style="left:265px;top:491px;background:#ccc"></span>
  <span class="dash abs" style="left:279px;top:491px;background:var(--gold-bright)"></span>

  <section class="seo-band abs" role="img" aria-label="Dark purple background with faint line-icon pattern of devices and media"></section>
  <h2 class="seo-title abs center">SEO COMPANY IN CLEVELAND, OHIO - SEARCH ENGINE<br>OPTIMIZATION SERVICES FOR LOCAL BUSINESSES IN OHIO</h2>
  <p class="seo-text abs center">Watch the Video Testimonial below from our client, the owner of one of Cleveland's and Akron's top Electrician<br>Companies! We love local businesses and want yours to grow like his business!</p>

  <h2 class="b2b-title abs center">GROWING B2B COMPANIES IS WHAT WE DO BEST</h2>
  <p class="b2b-copy abs" style="top:808px">Clients choose Vantorel Group because we get real results – new leads and sales. After 20+ years in business, our success stems from understanding B2B industries and knowing how to connect with online audiences. We're committed to advancing your company's growth.</p>
  <p class="b2b-copy abs" style="top:845px">From accounting and financial services to manufacturing companies, we captivate potential buyers and customers and get them to connect with our clients. You are innovators, engineers and problem solvers at heart. Your story is unique, and possibly decades old. But how convincing is your online brand? We will work with you to capitalize on your biggest asset – knowledge – to generate the right leads and new business.</p>

  <h3 class="gallery-label abs">PROJECT GALLERY</h3>
  <span class="dash abs" style="left:402px;top:917px;background:#ccc"></span>
  <span class="dash abs" style="left:414px;top:917px;background:var(--gold-bright)"></span>
  <div class="btn btn-purple gallery-btn abs">View gallery</div>
  <div class="shot abs" style="left:74px;background:linear-gradient(135deg,#2a2a2a,#555 60%,#3a3a3a)" role="img" aria-label="Project photo: wall of video screens in a dark room"></div>
  <div class="shot abs" style="left:177px;background:linear-gradient(135deg,#c9a98a,#e8e4df 55%,#b89a7f)" role="img" aria-label="Project photo: tablet showing analytics charts on a desk"></div>
  <div class="shot abs" style="left:281px;background:linear-gradient(135deg,#8a6a4c,#d9d6d0 50%,#7a5c42)" role="img" aria-label="Project photo: laptop, phone and papers on a wooden desk"></div>
  <div class="shot abs" style="left:384px;background:linear-gradient(135deg,#9fb3c8,#e6ecef 55%,#7f97b0)" role="img" aria-label="Project photo: hand writing online marketing notes on a screen"></div>

  <section class="cta abs" role="img" aria-label="Faded background of marketing word cloud and a tablet showing charts"></section>
  <h2 class="cta-title abs center">ARE YOU READY TO GROW YOUR COMPANY'S REVENUE<br>WITH DIGITAL MARKETING?</h2>
  <div class="btn btn-gold cta-gold abs">See result we have produced</div>
  <div class="btn btn-purple cta-purple abs">Let's chat</div>

  <section class="subscribe abs"></section>
  <h3 class="sub-title abs center">Subscribe to Happy Hour!</h3>
  <p class="sub-text abs center">Subscribe to our newsletter to ensure that your company website is pulling in traffic, learn about<br>our staff, and to get random facts each month!</p>
  <div class="field abs" style="left:143px">Enter Your Email</div>
  <div class="field abs" style="left:247px">Company Name</div>
  <div class="btn btn-purple sub-btn abs">Sign up</div>

  <footer class="site-footer abs"></footer>
  <div class="foot-contact abs">42 Larkspur Row, Valley City, OH 44000<br>Email : hello@fernwick.example<br>Phone : 555-014-2760</div>
  <span class="social abs" style="left:74px"></span>
  <span class="social abs" style="left:84px"></span>
  <span class="social abs" style="left:94px"></span>
  <div class="foot-brand abs center">
    <div class="foot-dot"></div>
    <div class="foot-name">FERNWICK</div>
    <div class="foot-tag">Digital Marketing Agency</div>
  </div>
  <div class="foot-links abs" style="top:1443px">Home &nbsp; Services &nbsp; Blog &nbsp; FAQ &nbsp; Contact Us</div>
  <div class="foot-links abs" style="top:1456px">Policy &nbsp;| &nbsp;Terms &amp; condition &nbsp;| &nbsp;Site map</div>
  <div class="foot-links abs" style="top:1470px;font-size:4px">© 2019 Fernwick . All rights reserved</div>

</main>
</div>
</body>
</html>
```